Modern, corporate management consultancy firm needs a new website

We need a website for an Australian based management consultancy firm.

The company name is Corbel Strategy Partners.

We are looking for a parallax style wordpress site.

The site needs to provide the following functions:

1) subscribe function
2) links to social media (twitter, linkedin and mail)
3) a gated document section where people can download pdf's from the site after registering or providing name, company, position, email and contact number.

Attached is the company logo, would like to see designs that incorporate the dark blue and silver in the logo and separated into the following sections (Home, About, Services (with 4 options), Our Team, Links, Contacts.

Need the site to be easy to navigate and updated.

Potentially a News Section that can be updated regularly.

Target Market(s)

Target market is SME, business owners and directors

Industry/Entity Type

Management Consulting

Coding

Coded - Design and coding required

Number of Pages Required

1 page

Font styles to use
Sans Serif

Colors
0255a3
cbcbcb
757575
000000

Requirements
Must have
• Must be easy to read and use
Nice to have
• Features are listed on initial brief

```html
<!DOCTYPE html>
<html lang="en">
<head>
<meta charset="utf-8">
<title>Corbel Strategy Partners — Business Improvement Specialists</title>
<link rel="stylesheet" href="https://fonts.googleapis.com/css2?family=Oswald:wght@500;600&family=Roboto:wght@300;400;500;700&display=swap">
<style>
  :root {
    --navy: #0255a3;
    --navy-deep: #0b2f5c;
    --navy-dark: #123a6a;
    --silver: #cbcbcb;
    --grey: #757575;
    --ink: #000000;
    --text: #3c3c3c;
    --footer: #1d1d1f;
    --footer-line: #2c2c2e;
    --white: #ffffff;
  }
  * { box-sizing: border-box; margin: 0; padding: 0; }
  html, body { width: 713px; height: 1200px; overflow: hidden; background: var(--white); }
  body { font-family: "Roboto", Arial, sans-serif; color: var(--text); }
  .page { position: relative; width: 713px; height: 1200px; overflow: hidden; }

  /* Hero */
  .hero { position: absolute; left: 0; top: 0; width: 713px; height: 333px; }
  .hero-photo { position: absolute; inset: 0;
    background: linear-gradient(180deg, #9fb6cc 0%, #6f8ea9 38%, #3f5f7c 68%, #2b4660 100%); }
  .main-nav { position: absolute; left: 0; top: 0; width: 100%; height: 43px;
    background: rgba(20, 30, 45, 0.55); }
  .main-nav a { position: absolute; top: 14px; font-size: 12px; font-weight: 500; letter-spacing: .5px;
    color: var(--white); text-decoration: none; transform: translateX(-50%); }
  .main-nav a.active { border-bottom: 2px solid var(--white); padding-bottom: 4px; }
  .brand { position: absolute; left: 0; right: 0; top: 100px; display: flex; justify-content: center;
    align-items: center; gap: 14px; }
  .brand-mark { width: 58px; height: 58px; border-radius: 50%; background: var(--navy-deep); }
  .brand-name { font-weight: 400; font-size: 30px; color: var(--white); line-height: 1.05; }
  .hero-title { position: absolute; left: 0; right: 0; top: 206px; text-align: center;
    font-family: "Oswald", "Arial Narrow", sans-serif; font-weight: 600; font-size: 40px;
    color: var(--white); letter-spacing: .5px; text-transform: uppercase; }
  .hero-notch { position: absolute; left: 321px; top: 311px; }

  /* Welcome */
  .welcome { position: absolute; left: 0; top: 333px; width: 713px; height: 289px; text-align: center; }
  .welcome h1 { margin-top: 32px; font-weight: 300; font-size: 30px; color: #4a4a4a; }
  .welcome h1 span { color: var(--navy); font-weight: 400; }
  .welcome .lead { margin: 16px auto 0; width: 560px; font-size: 13px; font-weight: 500; line-height: 19px; color: var(--navy); }
  .welcome .body { margin: 14px auto 0; width: 520px; font-size: 10px; line-height: 15px; color: var(--grey); }
  .btn-outline { display: inline-block; margin-top: 16px; padding: 8px 20px; border: 1.5px solid var(--navy);
    border-radius: 18px; font-size: 11px; font-weight: 500; color: var(--navy); letter-spacing: .5px; }

  /* Services */
  .services { position: absolute; left: 0; top: 622px; width: 713px; height: 305px;
    background: linear-gradient(135deg, #1c4b80 0%, var(--navy-dark) 55%, #0d2a4d 100%); }
  .services-photo { position: absolute; left: 0; top: 0; width: 330px; height: 305px;
    background: linear-gradient(90deg, rgba(150,175,205,.45) 0%, rgba(90,125,170,.3) 55%, rgba(18,58,106,0) 100%); }
  .services h2 { position: absolute; left: 350px; top: 20px; font-weight: 300; font-size: 28px; color: var(--white); }
  .service { position: absolute; width: 220px; color: var(--white); }
  .service svg { position: absolute; left: 0; top: 0; }
  .service h3 { margin-left: 42px; font-size: 14px; font-weight: 400; line-height: 17px; }
  .service p { margin: 6px 0 0 42px; font-size: 9.5px; line-height: 13px; color: var(--silver); }

  /* Download band */
  .download { position: absolute; left: 0; top: 927px; width: 713px; height: 90px; background: var(--white); }
  .download p { position: absolute; left: 48px; top: 20px; width: 420px; font-size: 19px; line-height: 25px; color: #2b2b2b; }
  .btn-solid { position: absolute; left: 500px; top: 24px; width: 165px; height: 40px; border-radius: 20px;
    background: var(--navy-deep); color: var(--white); font-size: 15px; font-weight: 500; letter-spacing: .3px;
    display: flex; align-items: center; justify-content: center; }

  /* Footer */
  .site-footer { position: absolute; left: 0; top: 1017px; width: 713px; height: 183px; background: var(--footer); color: var(--white); }
  .site-footer h4 { position: absolute; top: 24px; font-size: 16px; font-weight: 400; }
  .subscribe-title { left: 48px; }
  .connect-title { left: 388px; }
  .field { position: absolute; top: 58px; width: 138px; height: 22px; border: 1px solid #6a6a6a; background: #141416;
    font-size: 9px; color: #cfcfcf; padding: 5px 6px; }
  .field-first { left: 48px; }
  .field-last { left: 196px; }
  .btn-subscribe { position: absolute; left: 48px; top: 92px; width: 74px; height: 22px; background: var(--navy);
    border: 1px solid #7fa8d6; font-size: 10px; display: flex; align-items: center; justify-content: center; }
  .social { position: absolute; top: 65px; left: 388px; display: flex; gap: 20px; }
  .social span { width: 36px; height: 36px; border-radius: 50%; border: 1.5px solid #bdbdbd; display: flex; align-items: center; justify-content: center; }
  .legal { position: absolute; left: 0; right: 0; top: 150px; border-top: 1px solid var(--footer-line); padding-top: 10px;
    text-align: center; font-size: 9px; color: #9a9a9a; }
  .legal b { color: var(--white); font-weight: 500; }
</style>
</head>
<body>
<div class="page">

  <header class="hero">
    <div class="hero-photo" role="img" aria-label="Photo of a harbour city skyline at dusk"></div>
    <nav class="main-nav">
      <a class="active" style="left:107px">HOME</a>
      <a style="left:185px">ABOUT</a>
      <a style="left:273px">SERVICES</a>
      <a style="left:380px">OUR TEAM</a>
      <a style="left:452px">LINKS</a>
      <a style="left:542px">CONTACT</a>
    </nav>
    <div class="brand">
      <div class="brand-mark"></div>
      <div class="brand-name">Corbel Strategy<br>Partners</div>
    </div>
    <h2 class="hero-title">Business Improvement Specialists</h2>
    <svg class="hero-notch" width="72" height="22" viewBox="0 0 72 22">
      <path d="M0 22 Q36 -6 72 22 Z" fill="#ffffff"/>
      <path d="M29 11 L36 16 L43 11" fill="none" stroke="#333" stroke-width="2"/>
    </svg>
  </header>

  <section class="welcome">
    <h1>Welcome to <span>Corbel Strategy Partners</span></h1>
    <p class="lead">Providing tailored specialist advice to businesses, working together to identify problem areas, resolve issues and improve performance.</p>
    <p class="body">Corbel Strategy Partners is a boutique management consulting firm that serves micro, small and mid-cap listed and private companies.</p>
    <p class="body">We are a team of specialists in business and performance improvement, process optimisation, profit maximisation and negotiation/mediation.</p>
    <span class="btn-outline">READ MORE</span>
  </section>

  <section class="services">
    <div class="services-photo" role="img" aria-label="Photo of a hand pressing a touchscreen button"></div>
    <h2>Our Services</h2>

    <div class="service" style="left:210px; top:74px;">
      <svg width="30" height="30" viewBox="0 0 30 30" fill="none" stroke="#fff" stroke-width="2">
        <circle cx="15" cy="12" r="7"/><path d="M12 22h6M12.5 25h5M15 1v2M4 12H2M28 12h-2M6 4l1.5 1.5M24 4l-1.5 1.5"/>
      </svg>
      <h3>Business Health Checks</h3>
      <p>Corbel Strategy Partners provides a fixed fee health check for your business.</p>
    </div>

    <div class="service" style="left:452px; top:74px;">
      <svg width="30" height="30" viewBox="0 0 30 30" fill="none" stroke="#fff" stroke-width="2.5">
        <circle cx="11" cy="13" r="5"/><circle cx="22" cy="22" r="3.5"/>
        <path d="M11 4v3M11 19v3M2 13h3M17 13h3M22 15v2M22 27v2M15 22h2M27 22h2"/>
      </svg>
      <h3>Turnaround Management</h3>
      <p>Turnaround management is a process that uses analysis and planning to stabilise the business.</p>
    </div>

    <div class="service" style="left:210px; top:178px;">
      <svg width="30" height="30" viewBox="0 0 30 30" fill="none" stroke="#fff" stroke-width="2">
        <circle cx="10" cy="9" r="4"/><circle cx="21" cy="9" r="4"/>
        <path d="M3 24c0-5 3-8 7-8s7 3 7 8M14 24c0-5 3-8 7-8s7 3 7 8"/>
      </svg>
      <h3>Business Performance Consulting</h3>
      <p>Often times, we find that there are areas of a business which need attention.</p>
    </div>

    <div class="service" style="left:452px; top:178px;">
      <svg width="30" height="30" viewBox="0 0 30 30" fill="none" stroke="#fff" stroke-width="2">
        <path d="M2 14l6-5 6 3 6-3 8 5-6 6-4-3-4 3-6-1z"/><path d="M11 17l4 4M14 15l4 4"/>
      </svg>
      <h3>Independent Insolvency Advice</h3>
      <p>When a business encounters difficult financial circumstances, it can be a very stressful time.</p>
    </div>
  </section>

  <section class="download">
    <p>Lorem Ipsum is simply dummy text of the printing and typesetting industry.</p>
    <span class="btn-solid">DOWNLOAD PDF</span>
  </section>

  <footer class="site-footer">
    <h4 class="subscribe-title">Subscribe to Corbel Strategy Partners</h4>
    <div class="field field-first">Enter Name</div>
    <div class="field field-last">Enter Email</div>
    <div class="btn-subscribe">Subscribe</div>

    <h4 class="connect-title">Connect With Us</h4>
    <div class="social">
      <span aria-label="Share">
        <svg width="16" height="16" viewBox="0 0 16 16" fill="none" stroke="#fff" stroke-width="1.4">
          <circle cx="12" cy="3.5" r="2"/><circle cx="4" cy="8" r="2"/><circle cx="12" cy="12.5" r="2"/>
          <path d="M5.8 7l4.4-2.5M5.8 9l4.4 2.5"/>
        </svg>
      </span>
      <span aria-label="Profile">
        <svg width="16" height="16" viewBox="0 0 16 16" fill="none" stroke="#fff" stroke-width="1.4">
          <circle cx="8" cy="5" r="3"/><path d="M2.5 15c0-3.5 2.5-5.5 5.5-5.5s5.5 2 5.5 5.5"/>
        </svg>
      </span>
      <span aria-label="Careers">
        <svg width="16" height="14" viewBox="0 0 16 14" fill="none" stroke="#fff" stroke-width="1.4">
          <rect x="1" y="4" width="14" height="9" rx="1"/><path d="M5.5 4V2h5v2M1 8h14"/>
        </svg>
      </span>
      <span aria-label="Email">
        <svg width="16" height="12" viewBox="0 0 16 12" fill="none" stroke="#fff" stroke-width="1.4">
          <rect x="1" y="1" width="14" height="10" rx="1"/><path d="M1 1l7 6 7-6"/>
        </svg>
      </span>
    </div>

    <p class="legal">© <b>Corbel Strategy Partners</b> 2015. All Rights Reserved.</p>
  </footer>

</div>
</body>
</html>
```